Create book cover for a Sudoku puzzle book

It is a sudoku puzzle book for experienced sudoku puzzle solvers. It has over 250 sudoku puzzles ranging from medium level to hard.

Create a book cover closely refer to the reference image. The book cover must look as similar to the reference image as possible, including all the design style, color, illustrations and fonts. Use the sudoku puzzle in the attachment to replace the one on the reference image. All the design elements including fonts must be commercially licensed.

In the final delivery, the cover design must be available in both png/ai and pdf file format. All source files and commercial licenses for the used design elements must also be delivered as well.

Book Title: Gridwork for Devotees
Subtitle: 250+ Medium to Hard Puzzles

Book size: 8.5x11 inches
Page count: 171
Paperback Print Book
Platform: Bramlow PressDesk

Text on the front cover (all in uppercase):
- Gridwork for Devotees
- 250+ Medium to Hard Puzzles
- 2025
- 250+ Puzzles
- large print

Text on spine:
Book title (only title, no subtitle) on the upper part of the spine and author name on the lower part. All in uppercase.

Text on the back cover (on the top):
Thank you for purchasing "Gridwork for Devotees." We hope you are enjoying the puzzles and finding them both challenging and fun. If you have a moment, please consider leaving a review on Bramlow. Your feedback helps other puzzle enthusiasts discover this book and allows us to continue creating quality content. We appreciate your support and look forward to hearing your thoughts!

Logo on back cover:
-pen name logo, the logo size should be small and subtle. (on bottom middle)

```html
<!DOCTYPE html>
<html lang="en">
<head>
<meta charset="utf-8">
<title>Gridwork for Devotees – Cover Spread</title>
<link rel="stylesheet" href="https://fonts.googleapis.com/css2?family=Montserrat:wght@400;500;700;800;900&display=swap">
<style>
  :root {
    --stage: #939393;
    --paper: #ffffff;
    --ink: #0f171b;
    --red: #e0282e;
    --red-deep: #a5161b;
    --grey-soft: #cfd3d6;
  }
  * { box-sizing: border-box; margin: 0; padding: 0; }
  html, body { width: 1200px; height: 800px; overflow: hidden; }
  body {
    background: var(--stage);
    font-family: "Montserrat", sans-serif;
    color: var(--ink);
    position: relative;
  }

  /* ---------- back cover ---------- */
  .back-cover {
    position: absolute; left: 43px; top: 72px;
    width: 506px; height: 655px;
    background: var(--paper);
    overflow: hidden;
  }
  .back-brush { position: absolute; }
  .back-brush--top {
    left: 100px; top: -40px; width: 230px; height: 150px;
    background: radial-gradient(ellipse 50% 50% at 55% 30%, var(--ink) 0%, var(--ink) 40%, var(--red-deep) 55%, rgba(15,23,27,0.4) 70%, rgba(255,255,255,0) 100%);
  }
  .back-brush--corner {
    left: -40px; top: -40px; width: 110px; height: 110px;
    background: radial-gradient(circle at 30% 30%, var(--ink) 0%, rgba(15,23,27,0.6) 45%, rgba(255,255,255,0) 72%);
  }
  .back-brush--side {
    left: -30px; top: 40px; width: 60px; height: 230px;
    background: radial-gradient(ellipse 50% 50% at 30% 50%, rgba(15,23,27,0.8) 0%, rgba(15,23,27,0.3) 55%, rgba(255,255,255,0) 100%);
  }
  .back-brush--bottom {
    left: -30px; bottom: -40px; width: 250px; height: 90px;
    background: radial-gradient(ellipse 50% 50% at 30% 70%, var(--ink) 0%, rgba(15,23,27,0.5) 45%, rgba(255,255,255,0) 100%);
  }
  .back-message {
    position: absolute; left: 54px; top: 125px; width: 398px;
    font-size: 18.6px; font-weight: 500; line-height: 23.8px;
    text-align: justify;
  }
  .pen-name {
    position: absolute; left: 210px; top: 503px;
    width: 86px; height: 86px;
    border: 2.5px solid var(--ink); border-radius: 50%;
    display: flex; align-items: center; justify-content: center;
    font-size: 11px; font-weight: 700; letter-spacing: 0.3px;
    text-align: center; line-height: 1.1;
  }

  /* ---------- spine ---------- */
  .spine {
    position: absolute; left: 588px; top: 72px;
    width: 23px; height: 655px;
    background: var(--paper);
  }
  .spine-text {
    position: absolute; left: 0; width: 23px;
    writing-mode: vertical-rl;
    display: flex; align-items: center; justify-content: center;
    font-size: 15px; line-height: 23px; white-space: nowrap;
  }
  .spine-title { top: 90px; font-weight: 800; }
  .spine-author { top: 427px; font-weight: 500; }

  /* ---------- front cover ---------- */
  .front-cover {
    position: absolute; left: 651px; top: 72px;
    width: 506px; height: 655px;
    background: var(--paper);
    overflow: hidden;
  }
  .splash-art {
    position: absolute; left: 0; top: 140px; width: 506px; height: 470px;
    background:
      radial-gradient(ellipse 52% 48% at 50% 52%, var(--red) 0%, var(--red-deep) 30%, var(--ink) 55%, var(--red) 72%, rgba(255,255,255,0) 100%);
  }
  .kicker {
    position: absolute; top: 14px; width: 100%; text-align: center;
    font-size: 28px; font-weight: 800;
  }
  .title-main {
    position: absolute; top: 44px; width: 100%; text-align: center;
    font-size: 72px; font-weight: 900; letter-spacing: -1px; line-height: 1.2;
  }
  .title-sub {
    position: absolute; top: 120px; width: 100%; text-align: center;
    font-size: 28px; font-weight: 800;
  }
  .year-pill {
    position: absolute; left: 206px; top: 157px;
    width: 94px; height: 32px; border-radius: 12px;
    background: var(--ink); color: var(--paper);
    font-size: 27px; font-weight: 800;
    display: flex; align-items: center; justify-content: center;
  }
  .puzzle-grid {
    position: absolute; left: 160px; top: 270px;
    width: 177px; height: 174px;
    background: var(--paper);
    border: 2px solid var(--ink);
    display: grid;
    grid-template-columns: repeat(9, 1fr);
    grid-template-rows: repeat(9, 1fr);
  }
  .cell {
    border-right: 0.8px solid var(--ink);
    border-bottom: 0.8px solid var(--ink);
    font-size: 14px; font-weight: 500;
    display: flex; align-items: center; justify-content: center;
  }
  .cell:nth-child(9n) { border-right: none; }
  .cell:nth-child(9n+3), .cell:nth-child(9n+6) { border-right: 2px solid var(--ink); }
  .cell:nth-child(n+19):nth-child(-n+27),
  .cell:nth-child(n+46):nth-child(-n+54) { border-bottom: 2px solid var(--ink); }
  .cell:nth-child(n+73) { border-bottom: none; }

  .large-print {
    position: absolute; left: 356px; top: 465px;
    width: 118px; height: 118px;
  }
  .large-print svg { position: absolute; inset: 0; }
  .large-print-text {
    position: absolute; inset: 0;
    display: flex; flex-direction: column; align-items: center; justify-content: center;
    color: var(--paper); transform: rotate(8deg); line-height: 1.05;
  }
  .large-print-text .strong { font-size: 21px; font-weight: 900; }
  .large-print-text .light { font-size: 20px; font-weight: 400; }

  .bottom-band {
    position: absolute; left: 0; bottom: 0; width: 100%; height: 49px;
    background: var(--ink); color: var(--paper);
    display: flex; align-items: center; justify-content: center;
    font-size: 25px; font-weight: 800; letter-spacing: 0.2px;
  }
</style>
</head>
<body>

<section class="back-cover">
  <div class="back-brush back-brush--top" role="img" aria-label="Black and red ink brush strokes along the top edge"></div>
  <div class="back-brush back-brush--corner" role="img" aria-label="Black brush texture in the top corner"></div>
  <div class="back-brush back-brush--side" role="img" aria-label="Rough black brush texture along the left edge"></div>
  <div class="back-brush back-brush--bottom" role="img" aria-label="Black brush strokes in the bottom corner"></div>
  <p class="back-message">Thank you for purchasing "Gridwork for Devotees." We hope you are enjoying the puzzles and finding them both challenging and fun. If you have a moment, please consider leaving a review on Bramlow. Your feedback helps other puzzle enthusiasts discover this book and allows us to continue creating quality content. We appreciate your support and look forward to hearing your thoughts!</p>
  <div class="pen-name">ELIAS<br>VARDEN</div>
</section>

<section class="spine">
  <span class="spine-text spine-title">GRIDWORK FOR DEVOTEES</span>
  <span class="spine-text spine-author">ELIAS VARDEN</span>
</section>

<section class="front-cover">
  <div class="splash-art" role="img" aria-label="Explosive red, black and white paint splash radiating from the centre"></div>
  <p class="kicker">250+ PUZZLES</p>
  <h1 class="title-main">GRIDWORK</h1>
  <p class="title-sub">FOR DEVOTEES</p>
  <div class="year-pill">2025</div>

  <div class="puzzle-grid" aria-label="Sample puzzle">
    <div class="cell">5</div><div class="cell"></div><div class="cell"></div><div class="cell"></div><div class="cell">8</div><div class="cell"></div><div class="cell"></div><div class="cell"></div><div class="cell">2</div>
    <div class="cell"></div><div class="cell">7</div><div class="cell"></div><div class="cell">3</div><div class="cell"></div><div class="cell"></div><div class="cell">9</div><div class="cell"></div><div class="cell"></div>
    <div class="cell"></div><div class="cell"></div><div class="cell">4</div><div class="cell"></div><div class="cell"></div><div class="cell">6</div><div class="cell"></div><div class="cell">1</div><div class="cell"></div>
    <div class="cell">2</div><div class="cell"></div><div class="cell"></div><div class="cell">9</div><div class="cell"></div><div class="cell"></div><div class="cell"></div><div class="cell"></div><div class="cell">6</div>
    <div class="cell"></div><div class="cell">9</div><div class="cell"></div><div class="cell"></div><div class="cell">1</div><div class="cell"></div><div class="cell"></div><div class="cell">3</div><div class="cell"></div>
    <div class="cell">8</div><div class="cell"></div><div class="cell"></div><div class="cell"></div><div class="cell"></div><div class="cell">4</div><div class="cell"></div><div class="cell"></div><div class="cell">5</div>
    <div class="cell"></div><div class="cell">4</div><div class="cell"></div><div class="cell">6</div><div class="cell"></div><div class="cell"></div><div class="cell">7</div><div class="cell"></div><div class="cell"></div>
    <div class="cell"></div><div class="cell"></div><div class="cell">9</div><div class="cell"></div><div class="cell"></div><div class="cell">2</div><div class="cell"></div><div class="cell">5</div><div class="cell"></div>
    <div class="cell">6</div><div class="cell"></div><div class="cell"></div><div class="cell"></div><div class="cell">7</div><div class="cell"></div><div class="cell"></div><div class="cell"></div><div class="cell">3</div>
  </div>

  <div class="large-print">
    <svg viewBox="0 0 100 100" aria-hidden="true">
      <polygon fill="#ffffff" points="50,0 56,9 66,3 69,14 80,11 79,22 91,23 86,33 97,38 89,46 98,53 89,60 95,69 84,72 86,83 75,83 73,94 63,90 57,100 50,92 43,100 37,90 27,94 25,83 14,83 16,72 5,69 11,60 2,53 11,46 3,38 14,33 9,23 21,22 20,11 31,14 34,3 44,9"/>
      <polygon fill="#e0282e" transform="translate(50 50) scale(0.9) translate(-50 -50)" points="50,0 56,9 66,3 69,14 80,11 79,22 91,23 86,33 97,38 89,46 98,53 89,60 95,69 84,72 86,83 75,83 73,94 63,90 57,100 50,92 43,100 37,90 27,94 25,83 14,83 16,72 5,69 11,60 2,53 11,46 3,38 14,33 9,23 21,22 20,11 31,14 34,3 44,9"/>
    </svg>
    <div class="large-print-text">
      <span class="strong">LARGE</span>
      <span class="light">PRINT</span>
    </div>
  </div>

  <div class="bottom-band">250+ MEDIUM TO HARD PUZZLES</div>
</section>

</body>
</html>
```